Packaging Design job - Product : Supplement for Travel Sickness

We need a packaging design for a travel sickness supplement called "VOLUMAR"

VOLUMAR It is a dietary supplement based on ginger which has properties fighting against motion sickness.

Ginger is a root used for many years for its beneficial effects on health. In addition to its stimulating and toning properties which help to resist fatigue, ginger is used as an adjuvant in case of nausea, vomiting and motion sickness. Ideal for pregnant women to combat certain disadvantages of pregnancy.

This product will be in blister form of 30 capsules. We need for this a packaging design for the box.Dimensions: 100 * 20 * 200 mm

We would like to see clean, modern and fresh designs.This should give the impression of professional products of pharmaceutical quality. You will also find attached the logo of our company.Ps : You can change the color of the logo

Mention to put on the box :

• Produit en France: Laboratoire KRANIVO, 24 Rue des Lavandières 37410 BRÉCHAL
• Distribué au Maroc: LUMORAXIN 14 rue Oumaima Tazrouti 30050 FEZ MAROC
• Complément alimentaire, ce n'est pas un médicament
• Voie orale
• Tenir hors de portée des enfants
• Respectez la dose recommandée
• Ce produit ne remplace pas une alimentation variée

Mode d'utilisation (How to use) :

2 à 3 gélules 30 min avant de prendre le véhicule de transport
1 gélule par jour en cas de cure

Font styles to use
Serif
Sans Serif
Script

Requirements
Should not have
• Sales and other "must buy" "guaranteed" etc

```html
<!DOCTYPE html>
<html lang="en">
<head>
<meta charset="utf-8">
<title>VOLUMAR – box panels</title>
<link rel="stylesheet" href="https://fonts.googleapis.com/css2?family=Montserrat:ital,wght@0,500;0,700;0,800;0,900;1,900&family=Josefin+Sans:wght@300;400&display=swap">
<style>
  :root {
    --teal: #1bb9b5;
    --teal-deep: #14a8a4;
    --white: #ffffff;
    --paper: #f6f7f7;
    --rule: #8e8e8e;
    --pill: #8a8f91;
    --ink-soft: #9aa3a5;
    --illus-a: #f3f4f4;
    --illus-b: #dfe3e3;
  }
  * { margin: 0; padding: 0; box-sizing: border-box; }
  html, body { width: 1200px; height: 1200px; overflow: hidden; }
  body {
    background: var(--paper);
    font-family: "Montserrat", sans-serif;
    position: relative;
  }

  /* Front face of the box */
  .front-panel {
    position: absolute;
    left: 100px;
    top: 250px;
    width: 1000px;
    height: 470px;
    background: var(--teal);
    overflow: hidden;
  }
  .front-panel__header {
    position: absolute;
    left: 0; top: 0;
    width: 100%;
    height: 150px;
    background: var(--white);
  }
  .front-panel__rule {
    position: absolute;
    left: 0; top: 14px;
    width: 100%;
    height: 3px;
    background: var(--rule);
  }
  .brand {
    position: absolute;
    right: 44px;
    top: 52px;
    display: flex;
    flex-direction: column;
    align-items: flex-end;
  }
  .brand__row { display: flex; align-items: center; gap: 10px; }
  .brand__dot {
    width: 18px; height: 18px;
    border-radius: 50%;
    background: var(--teal);
  }
  .brand__name {
    font-weight: 800;
    font-size: 32px;
    letter-spacing: 1px;
    color: var(--teal);
  }
  .brand__tagline {
    margin-top: 4px;
    font-family: "Josefin Sans", sans-serif;
    font-size: 10px;
    letter-spacing: 1.5px;
    color: var(--ink-soft);
    text-transform: uppercase;
  }

  .product-name {
    position: absolute;
    left: 50px;
    top: 168px;
    font-weight: 900;
    font-size: 96px;
    line-height: 1;
    letter-spacing: 2px;
    color: var(--white);
  }
  .product-claim {
    position: absolute;
    left: 52px;
    top: 286px;
    width: 520px;
    font-family: "Josefin Sans", sans-serif;
    font-weight: 300;
    font-size: 19px;
    line-height: 1.35;
    color: var(--white);
  }
  .pack-count {
    position: absolute;
    left: 52px;
    top: 362px;
    padding: 6px 16px 5px;
    border-radius: 20px;
    background: var(--pill);
    color: var(--white);
    font-weight: 700;
    font-size: 13px;
    letter-spacing: 1px;
  }
  .ginger-illustration {
    position: absolute;
    right: 70px;
    top: 150px;
    width: 230px;
    height: 230px;
    border-radius: 50%;
    background: radial-gradient(circle at 45% 40%, var(--illus-a), var(--illus-b));
    border: 2px solid var(--white);
  }

  /* Side face of the box */
  .side-panel {
    position: absolute;
    left: 100px;
    top: 740px;
    width: 1000px;
    height: 160px;
    background: var(--teal-deep);
    display: flex;
    align-items: center;
    justify-content: center;
  }
  .side-panel__name {
    font-weight: 900;
    font-style: italic;
    font-size: 64px;
    letter-spacing: 2px;
    color: var(--white);
  }
</style>
</head>
<body>
  <section class="front-panel">
    <div class="front-panel__header">
      <div class="front-panel__rule"></div>
      <div class="brand">
        <div class="brand__row">
          <span class="brand__dot"></span>
          <span class="brand__name">LUMORAXIN</span>
        </div>
        <span class="brand__tagline">herbal wellness and nutrition</span>
      </div>
    </div>

    <h1 class="product-name">VOLUMAR</h1>
    <p class="product-claim">VOLUMAR It is a dietary supplement based on ginger which has properties fighting against motion sickness.</p>
    <span class="pack-count">30 CAPSULES</span>

    <div class="ginger-illustration" role="img" aria-label="Line drawing of a ginger root with leaves"></div>
  </section>

  <section class="side-panel">
    <span class="side-panel__name">VOLUMAR</span>
  </section>
</body>
</html>
```